Bref créative
Business Cards/Stationary Vandorik Law, P.C.
Professional
Colvin R. Vandorik
Attorney & Counselor at Law
489 Pellham Avenue
Worcester, Massachusetts 01604
Colvin@Vandorik-example.com
www.Vandorik-example.com
I would also like designs to include letterhead and envelopes. Thank you.
Would like to list the areas of practice on the back, Workers' Compensation, Car Accidents, Personal Injury, Family Law, Criminal Law

```html
<!DOCTYPE html>
<html lang="en">
<head>
<meta charset="utf-8">
<title>Vandorik Law, P.C. — Stationery</title>
<link rel="stylesheet" href="https://fonts.googleapis.com/css2?family=Libre+Baskerville:wght@400;700&family=Open+Sans:wght@400;600&display=swap">
<style>
  :root {
    --brand-blue: #1f3f94;
    --brand-blue-dark: #173274;
    --ink: #4a4a4a;
    --ink-light: #7a7a7a;
    --paper: #ffffff;
    --backdrop: #e6e7ea;
    --rule: #c9cdd8;
  }
  * { box-sizing: border-box; margin: 0; padding: 0; }
  html, body {
    width: 1200px; height: 799px; overflow: hidden;
    background: var(--backdrop);
    font-family: "Open Sans", Arial, sans-serif;
    color: var(--ink);
  }
  address { font-style: normal; }
  .sheet {
    position: absolute;
    background: var(--paper);
    box-shadow: 0 2px 10px rgba(0,0,0,.12);
  }
  .wordmark {
    font-family: "Libre Baskerville", Georgia, serif;
    font-weight: 700;
    color: var(--brand-blue);
    letter-spacing: .04em;
    line-height: 1.1;
    display: flex; align-items: center; gap: 8px;
    white-space: nowrap;
  }
  .wordmark .dot {
    display: inline-block; border-radius: 50%;
    background: var(--brand-blue); flex: none;
  }

  /* Letterhead */
  .letterhead { left: 50px; top: 40px; width: 440px; height: 569px; padding: 36px 40px; font-size: 8px; line-height: 1.55; }
  .letterhead-header {
    display: flex; justify-content: space-between; align-items: flex-start; gap: 16px;
  }
  .letterhead .wordmark { font-size: 17px; }
  .letterhead .wordmark .dot { width: 24px; height: 24px; }
  .letterhead-address {
    text-align: right; font-size: 7px; line-height: 1.6; color: var(--ink-light);
    border-left: 1px solid var(--rule); padding-left: 10px; white-space: nowrap;
  }
  .letter-date { margin-top: 40px; }
  .letter-recipient { margin-top: 14px; }
  .letter-salutation { margin-top: 14px; }
  .letter-body p { margin-top: 10px; text-align: justify; }
  .letter-closing { margin-top: 18px; }
  .letter-signer { margin-top: 30px; font-family: "Libre Baskerville", Georgia, serif; color: var(--brand-blue); font-size: 10px; }
  .letter-signer-title { color: var(--ink-light); }
  .letterhead-footer {
    position: absolute; left: 40px; right: 40px; bottom: 26px;
    border-top: 2px solid var(--brand-blue); padding-top: 6px;
    display: flex; justify-content: space-between; font-size: 7px; color: var(--ink-light);
  }

  /* Envelopes */
  .envelope-front { left: 530px; top: 40px; width: 620px; height: 260px; padding: 28px 32px; }
  .envelope-front .wordmark { font-size: 17px; }
  .envelope-front .wordmark .dot { width: 18px; height: 18px; }
  .envelope-return { margin-top: 8px; font-size: 7.5px; line-height: 1.6; color: var(--ink-light); }
  .envelope-front .envelope-rule {
    position: absolute; left: 32px; bottom: 26px; width: 220px; height: 2px; background: var(--brand-blue);
  }

  .envelope-back { left: 530px; top: 320px; width: 620px; height: 260px; overflow: hidden; }
  .envelope-back svg { position: absolute; inset: 0; }
  .envelope-back .wordmark {
    position: absolute; left: 50%; top: 34px; transform: translateX(-50%);
    color: var(--paper); font-size: 16px;
  }

  /* Business cards */
  .card { width: 280px; height: 160px; top: 610px; }
  .card-front { left: 530px; padding: 20px 18px; display: flex; gap: 14px; }
  .card-front .wordmark { font-size: 12px; flex-direction: column; align-items: flex-start; gap: 6px; width: 92px; }
  .card-front .wordmark .dot { width: 26px; height: 26px; }
  .card-details { border-left: 1px solid var(--rule); padding-left: 12px; font-size: 7px; line-height: 1.7; color: var(--ink-light); height: 112px; }
  .card-name { font-family: "Libre Baskerville", Georgia, serif; font-size: 10px; color: var(--brand-blue); font-weight: 700; line-height: 1.3; white-space: nowrap; }
  .card-title { font-size: 7.5px; margin-bottom: 8px; color: var(--ink); white-space: nowrap; }
  .card-contact { display: flex; align-items: flex-start; gap: 5px; white-space: nowrap; }
  .card-contact svg { width: 8px; height: 8px; margin-top: 3px; fill: var(--brand-blue); flex: none; }
  .card-front .card-band { position: absolute; left: 0; right: 0; bottom: 0; height: 8px; background: var(--brand-blue); }

  .card-back {
    left: 870px; background: var(--brand-blue); color: var(--paper);
    display: flex; flex-direction: column; align-items: center; justify-content: center; text-align: center;
  }
  .card-back-heading { font-family: "Libre Baskerville", Georgia, serif; font-size: 10px; letter-spacing: .12em; text-transform: uppercase; margin-bottom: 8px; }
  .practice-areas { list-style: none; font-size: 8.5px; line-height: 1.7; }
  .card-back-rule { width: 60px; height: 1px; background: rgba(255,255,255,.6); margin: 8px 0 6px; }
  .card-back-firm { font-family: "Libre Baskerville", Georgia, serif; font-size: 8px; letter-spacing: .08em; }
</style>
</head>
<body>

<section class="sheet letterhead" aria-label="Letterhead">
  <header class="letterhead-header">
    <div class="wordmark"><span class="dot"></span><span>VANDORIK<br>LAW, P.C.</span></div>
    <address class="letterhead-address">
      489 Pellham Avenue<br>
      Worcester, Massachusetts 01604<br>
      Colvin@Vandorik-example.com<br>
      www.Vandorik-example.com
    </address>
  </header>

  <p class="letter-date">March 4, 2024</p>
  <p class="letter-recipient">Mr. Daniel Okafor<br>27 Linden Court<br>Boston, MA 02108</p>
  <p class="letter-salutation">Dear Mr. Okafor,</p>
  <div class="letter-body">
    <p>Thank you for meeting with our office last week regarding your workers' compensation claim. We have reviewed the documents you provided and believe you have a strong basis to proceed.</p>
    <p>Enclosed please find a summary of the next steps, along with the forms that require your signature. Please return them at your earliest convenience so we may file on time.</p>
    <p>Should you have any questions, do not hesitate to contact me directly.</p>
  </div>
  <p class="letter-closing">Sincerely,</p>
  <p class="letter-signer">Colvin R. Vandorik</p>
  <p class="letter-signer-title">Attorney &amp; Counselor at Law</p>

  <footer class="letterhead-footer">
    <span>489 Pellham Avenue, Worcester, Massachusetts 01604</span>
    <span>www.Vandorik-example.com</span>
  </footer>
</section>

<section class="sheet envelope-front" aria-label="Envelope front">
  <div class="wordmark"><span class="dot"></span>VANDORIK LAW, P.C.</div>
  <address class="envelope-return">
    489 Pellham Avenue<br>
    Worcester, Massachusetts 01604
  </address>
  <div class="envelope-rule"></div>
</section>

<section class="sheet envelope-back" aria-label="Envelope back">
  <svg width="620" height="260" viewBox="0 0 620 260" aria-hidden="true">
    <path d="M0 0 H620 V40 L330 150 Q310 158 290 150 L0 40 Z" fill="var(--brand-blue)"/>
    <path d="M0 260 L290 150 M620 260 L330 150" stroke="var(--rule)" stroke-width="1" fill="none"/>
  </svg>
  <div class="wordmark">VANDORIK</div>
</section>

<section class="sheet card card-front" aria-label="Business card front">
  <div class="wordmark"><span class="dot"></span>VANDORIK<br>LAW, P.C.</div>
  <div class="card-details">
    <p class="card-name">Colvin R. Vandorik</p>
    <p class="card-title">Attorney &amp; Counselor at Law</p>
    <p class="card-contact">
      <svg viewBox="0 0 10 10"><path d="M5 0a3.5 3.5 0 0 0-3.5 3.5C1.5 6 5 10 5 10s3.5-4 3.5-6.5A3.5 3.5 0 0 0 5 0zm0 5a1.5 1.5 0 1 1 0-3 1.5 1.5 0 0 1 0 3z"/></svg>
      <span>489 Pellham Avenue<br>Worcester, MA 01604</span>
    </p>
    <p class="card-contact">
      <svg viewBox="0 0 10 10"><path d="M0 2h10v6H0z M0 2l5 3.5L10 2" fill="none" stroke="var(--brand-blue)" stroke-width="1"/></svg>
      Colvin@Vandorik-example.com
    </p>
    <p class="card-contact">
      <svg viewBox="0 0 10 10"><circle cx="5" cy="5" r="4.3" fill="none" stroke="var(--brand-blue)" stroke-width="1"/><path d="M1 5h8M5 .7c-2 2.5-2 6.1 0 8.6M5 .7c2 2.5 2 6.1 0 8.6" fill="none" stroke="var(--brand-blue)" stroke-width=".8"/></svg>
      www.Vandorik-example.com
    </p>
  </div>
  <div class="card-band"></div>
</section>

<section class="sheet card card-back" aria-label="Business card back">
  <p class="card-back-heading">Areas of Practice</p>
  <ul class="practice-areas">
    <li>Workers' Compensation</li>
    <li>Car Accidents &middot; Personal Injury</li>
    <li>Family Law &middot; Criminal Law</li>
  </ul>
  <div class="card-back-rule"></div>
  <p class="card-back-firm">VANDORIK LAW, P.C.</p>
</section>

</body>
</html>
```